Petroleum Trading Company Biz Card

We are a physical trading company for petroleum products such as diesel and gasoline. We need our business cards revamped and the designer is welcome to refine the logo as well. I included png and ai files of the current logo as well as PDF of the current card layout. The card just looks to amateurish (wrong fonts, bad layout etc). The logo is decent but we are open to adjustments to it as well.
Target Market(s)
trading, finance
Contact Information for Business Card
Professional looking card is a must. Clean crisp design and layout. Thanks
Colors
Designer to choose colors to be used in the design.
Look and feel

```html
<!DOCTYPE html>
<html lang="en">
<head>
<meta charset="utf-8">
<title>Meridian Fuels – Business Card</title>
<link href="https://fonts.googleapis.com/css2?family=Montserrat:wght@400;500;600;700;800&display=swap" rel="stylesheet">
<style>
  :root {
    --navy: #1d4c9a;
    --navy-deep: #173f82;
    --sky: #3fb2e8;
    --red: #e2343b;
    --paper: #ffffff;
    --mist: #ebebec;
    --ink: #1f3f7a;
    --stage: #2a2a2c;
  }
  * { box-sizing: border-box; margin: 0; padding: 0; }
  html, body { width: 1200px; height: 660px; overflow: hidden; }
  body {
    background: var(--stage);
    font-family: "Montserrat", sans-serif;
    display: flex;
    align-items: center;
    justify-content: center;
    gap: 40px;
  }
  .card {
    width: 520px;
    height: 297px;
    position: relative;
    overflow: hidden;
    background: var(--paper);
    box-shadow: 0 14px 30px rgba(0,0,0,.45);
  }

  /* Front */
  .front .band { position: absolute; left: 0; right: 0; background: var(--navy); }
  .front .band-top { top: 0; height: 70px; }
  .front .band-bottom { bottom: 0; height: 70px; }
  .front .rule { position: absolute; left: 0; right: 0; height: 3px; }
  .front .rule-sky-top { top: 70px; background: var(--sky); height: 5px; }
  .front .rule-red-top { top: 82px; background: var(--red); height: 2px; }
  .front .rule-red-bottom { bottom: 82px; background: var(--red); height: 2px; }
  .front .rule-sky-bottom { bottom: 70px; background: var(--sky); height: 5px; }
  .front .brand {
    position: absolute; inset: 84px 0; display: flex; align-items: center; justify-content: center;
  }

  .wordmark {
    font-weight: 800;
    color: var(--navy);
    letter-spacing: 1px;
    display: flex;
    align-items: center;
    gap: 10px;
    white-space: nowrap;
  }
  .wordmark .dot { width: 14px; height: 14px; border-radius: 50%; background: var(--red); flex: none; }
  .front .wordmark { font-size: 34px; }

  /* Back */
  .back .upper {
    position: absolute; top: 0; left: 0; right: 0; height: 150px;
    background: var(--mist);
    display: flex; align-items: center; justify-content: center;
  }
  .back .upper .wordmark { font-size: 30px; }
  .back .divider-red { position: absolute; top: 150px; left: 0; right: 0; height: 2px; background: var(--red); }
  .back .motif {
    position: absolute; left: 40px; top: 158px; width: 120px; height: 139px;
    border-radius: 60px 60px 0 0;
    background: linear-gradient(160deg, rgba(63,178,232,.28), rgba(226,52,59,.18) 60%, rgba(29,76,154,.15));
  }
  .back .person { position: absolute; left: 60px; top: 200px; }
  .back .name { font-size: 19px; color: var(--ink); font-weight: 700; letter-spacing: .3px; }
  .back .name span { font-weight: 400; }
  .back .role { font-size: 9px; color: var(--red); font-weight: 600; letter-spacing: 2px; margin-top: 2px; }
  .back .vline { position: absolute; left: 300px; top: 168px; width: 1px; height: 108px; background: var(--ink); }
  .back .contact { position: absolute; left: 315px; top: 162px; font-size: 10.5px; color: var(--ink); }
  .back .contact li { list-style: none; display: flex; align-items: center; gap: 7px; line-height: 15px; }
  .back .contact svg { width: 10px; height: 10px; flex: none; }
  .back .address { margin-top: 8px; font-size: 10px; font-weight: 600; line-height: 13px; color: var(--ink); }
  .back .address strong { font-weight: 700; }
</style>
</head>
<body>

  <section class="card front" aria-label="Card front">
    <div class="band band-top"></div>
    <div class="rule rule-sky-top"></div>
    <div class="rule rule-red-top"></div>
    <div class="brand">
      <div class="wordmark"><span class="dot"></span>MERIDIAN FUELS</div>
    </div>
    <div class="rule rule-red-bottom"></div>
    <div class="rule rule-sky-bottom"></div>
    <div class="band band-bottom"></div>
  </section>

  <section class="card back" aria-label="Card back">
    <div class="upper">
      <div class="wordmark"><span class="dot"></span>MERIDIAN FUELS LLC</div>
    </div>
    <div class="divider-red"></div>
    <div class="motif" role="img" aria-label="Soft brand-colour decorative shape"></div>

    <div class="person">
      <p class="name">DANIEL<span>HARTWELL</span></p>
      <p class="role">CHIEF EXECUTIVE OFFICER</p>
    </div>

    <div class="vline"></div>

    <div class="contact">
      <ul>
        <li><svg viewBox="0 0 10 10"><path d="M1 3c0-1 1-2 4-2s4 1 4 2v1H7V3H3v1H1z M2 5h6l1 4H1z" fill="#e2343b"/></svg>800.555.0142</li>
        <li><svg viewBox="0 0 10 10"><rect x="2.5" y=".5" width="5" height="9" rx="1" fill="none" stroke="#e2343b"/><circle cx="5" cy="8" r=".6" fill="#e2343b"/></svg>555.310.0187</li>
        <li><svg viewBox="0 0 10 10"><rect x="2.5" y=".5" width="5" height="9" rx="1" fill="none" stroke="#e2343b"/><circle cx="5" cy="8" r=".6" fill="#e2343b"/></svg>555.720.4416</li>
        <li><svg viewBox="0 0 10 10"><rect x=".5" y="2" width="9" height="6.5" fill="#e2343b"/><path d="M.5 2l4.5 3.5L9.5 2" fill="none" stroke="#fff" stroke-width=".8"/></svg>dhartwell@meridianfuels.co</li>
        <li><svg viewBox="0 0 10 10"><circle cx="5" cy="5" r="4.3" fill="none" stroke="#e2343b"/><ellipse cx="5" cy="5" rx="1.8" ry="4.3" fill="none" stroke="#e2343b" stroke-width=".7"/><path d="M.7 5h8.6" stroke="#e2343b" stroke-width=".7"/></svg>www.meridianfuels.co</li>
      </ul>
      <p class="address"><strong>Meridian Fuels, LLC</strong><br>250 Harbor Point Drive Suite 1400<br>Coral Bay, FL 33010</p>
    </div>
  </section>

</body>
</html>
```